Sympathy Gift Supplier needs packaging designs

We provide sympathy/bereavement gifts such as memorial candles and picture frames for those who recently lost a loved one. We need packaging design for our boxes that will be uplifting and positive, yet elegant.

We have attached our logo in white and black as well as a saying we would like on the box, and what we need on the back panel.
Ignore the black as it was something we were working on for another product.

Target Market(s)

These products will be given as gifts to people who lost a loved one as remembrance.

Requirements
Must have
• Back panel details (provided)
Memorial quote (provided)
Must be appropriate for this type of product

```html
<!DOCTYPE html>
<html lang="en">
<head>
<meta charset="utf-8">
<title>Serene Haven – Back Panel</title>
<link rel="stylesheet" href="https://fonts.googleapis.com/css2?family=Montserrat+Alternates:wght@300;400;600;700&display=swap">
<style>
  :root {
    --lavender-panel: #d6d7eb;
    --paper: #ffffff;
    --band-deep: #8585b5;
    --band-soft: #9696c5;
    --ink: #9c9bca;
    --ink-strong: #9594c6;
    --brand: #6b3596;
    --petal: #eceaf5;
    --petal-shade: #c9c8e2;
    --stem: #9fb8ad;
  }
  * { margin: 0; padding: 0; box-sizing: border-box; }
  html, body {
    width: 1200px; height: 772px; overflow: hidden;
    background: var(--paper);
    font-family: "Montserrat Alternates", "Montserrat", sans-serif;
    font-weight: 300;
    color: var(--ink);
  }
  .panel { position: relative; width: 1200px; height: 772px; }

  .info-side {
    position: absolute; left: 0; top: 0; width: 813px; height: 772px;
    background: var(--lavender-panel);
  }
  .footer-band {
    position: absolute; left: 0; top: 691px; width: 1200px; height: 32px;
    background: var(--band-deep);
  }
  .footer-band .band-right {
    position: absolute; left: 813px; top: 0; width: 387px; height: 32px;
    background: var(--band-soft);
  }

  .warning, .instructions {
    position: absolute; left: 0; width: 813px; text-align: center;
    font-size: 18.5px; line-height: 1.15;
  }
  .warning { top: 282px; }
  .instructions { top: 438px; }
  .panel-heading {
    font-weight: 700; font-size: 17.5px; color: var(--ink-strong);
    letter-spacing: 0.3px; margin-bottom: 8px;
  }
  .warning p { margin-bottom: 9px; }
  .instructions p { margin-bottom: 9px; }

  .brand-story {
    position: absolute; left: 862px; top: 80px; width: 300px;
  }
  .brand-name {
    font-size: 26px; font-weight: 400; color: var(--brand);
    margin-bottom: 14px;
  }
  .brand-story p { font-size: 19px; line-height: 21.6px; }

  .flower-art {
    position: absolute; left: 771px; top: 300px; width: 190px; height: 472px;
  }

  .brand-mark {
    position: absolute; left: 985px; top: 590px;
    display: flex; align-items: center; gap: 10px;
    font-size: 24px; font-weight: 400; color: var(--brand);
  }
  .brand-mark .dot {
    width: 18px; height: 18px; border-radius: 50%; background: var(--brand);
  }

  .web-address {
    position: absolute; right: 45px; top: 698px;
    font-size: 17px; font-weight: 700; color: var(--paper); letter-spacing: 0.2px;
  }
  .origin {
    position: absolute; right: 48px; top: 736px;
    font-size: 15px; font-weight: 400; color: var(--ink);
  }
</style>
</head>
<body>
<div class="panel">
  <div class="info-side"></div>
  <div class="footer-band"><div class="band-right"></div></div>

  <section class="warning">
    <h2 class="panel-heading">WARNING</h2>
    <p>Burn within sight. Keep away from flammable objects.</p>
    <p>Keep away from children and pets.</p>
  </section>

  <section class="instructions">
    <h2 class="panel-heading">Burning Instructions:</h2>
    <p>Trim wick to 1/4" before lighting.</p>
    <p>Keep candle free of any foreign materials including<br>matches and wick trimmings.</p>
    <p>Only burn the candle on a level, fire resistant surface.</p>
    <p>Do not burn candle for more than four hours at a time.</p>
    <p>Stop use when only 1/4" of wax remains.</p>
  </section>

  <section class="brand-story">
    <h1 class="brand-name">Serene Haven</h1>
    <p>is a family owned company &amp; all of our products are carefully designed &amp; crafted with your family in mind.</p>
  </section>

  <svg class="flower-art" role="img" aria-label="Watercolour illustration of white lisianthus flowers on green stems" viewBox="0 0 190 472">
    <defs>
      <linearGradient id="bloom-tone" x1="0" y1="0" x2="0" y2="1">
        <stop offset="0" stop-color="var(--petal)"/>
        <stop offset="0.55" stop-color="var(--petal-shade)"/>
        <stop offset="1" stop-color="var(--stem)" stop-opacity="0.6"/>
      </linearGradient>
    </defs>
    <rect width="190" height="472" rx="20" fill="url(#bloom-tone)" opacity="0.7"/>
  </svg>

  <div class="brand-mark"><span class="dot"></span>Serene Haven</div>

  <div class="web-address">www.SereneHaven.com</div>
  <div class="origin">MADE IN CHINA</div>
</div>
</body>
</html>
```